Brightmoor Security Solutions window graphic

Looking for a graphic for my security company , Business for the back window of my truck. Make it look cool, please.

Call now for service (206) 555-0147
Brightmoorsecuritywa.example

“ Protection you can count on”

Target Market(s)

Auto security

Industry/Entity Type

Security

```html
<!DOCTYPE html>
<html lang="en">
<head>
<meta charset="utf-8">
<title>Brightmoor Security Solutions – Rear Window Graphic</title>
<link rel="stylesheet" href="https://fonts.googleapis.com/css2?family=Bebas+Neue&family=Orbitron:wght@700;900&display=swap">
<style>
  :root {
    --brand-orange: #ef4b23;
    --slate: #36444f;
    --white: #ffffff;
    --page: #ffffff;
  }
  * { margin: 0; padding: 0; box-sizing: border-box; }
  html, body {
    width: 893px;
    height: 1200px;
    overflow: hidden;
    background: var(--page);
  }
  .canvas {
    position: relative;
    width: 893px;
    height: 1200px;
  }
  .window-graphic {
    position: absolute;
    left: 114px;
    top: 483px;
    width: 665px;
    height: 234px;
    background: var(--brand-orange);
    overflow: hidden;
  }
  .window-graphic__shape {
    position: absolute;
    inset: 0;
    width: 100%;
    height: 100%;
  }
  .brand {
    position: absolute;
    left: 66px;
    top: 30px;
    width: 214px;
    text-align: center;
  }
  .brand__mark {
    display: block;
    width: 62px;
    height: 62px;
    margin: 0 auto 38px;
    border-radius: 50%;
    background: var(--brand-orange);
  }
  .brand__name {
    font-family: "Orbitron", sans-serif;
    font-weight: 900;
    color: var(--brand-orange);
    line-height: 1;
  }
  .brand__name-main {
    display: block;
    font-size: 20px;
    letter-spacing: 0.5px;
  }
  .brand__name-sub {
    display: block;
    margin-top: 6px;
    font-size: 8.6px;
    letter-spacing: 2.6px;
  }
  .tagline {
    position: absolute;
    left: 80px;
    top: 188px;
    width: 186px;
    text-align: center;
    font-family: "Orbitron", sans-serif;
    font-weight: 900;
    font-size: 12px;
    line-height: 15px;
    letter-spacing: 1.2px;
    color: var(--slate);
  }
  .cta {
    position: absolute;
    left: 290px;
    top: 35px;
    width: 312px;
    text-align: center;
  }
  .cta__badge {
    display: inline-block;
    height: 43px;
    padding: 0 24px;
    background: var(--brand-orange);
    transform: skewX(-12deg);
  }
  .cta__badge-text {
    display: block;
    transform: skewX(12deg);
    font-family: "Bebas Neue", sans-serif;
    font-style: italic;
    font-size: 40px;
    line-height: 46px;
    color: var(--white);
    letter-spacing: 1px;
  }
  .cta__service {
    margin-top: 9px;
    font-family: "Bebas Neue", sans-serif;
    font-size: 54px;
    line-height: 46px;
    color: var(--slate);
  }
  .cta__phone {
    margin-top: 8px;
    font-family: "Bebas Neue", sans-serif;
    font-size: 58px;
    line-height: 48px;
    color: var(--slate);
    letter-spacing: 0.5px;
  }
  .cta__web {
    margin-top: 6px;
    font-family: "Bebas Neue", sans-serif;
    font-size: 20px;
    line-height: 22px;
    letter-spacing: 2.4px;
    color: var(--brand-orange);
  }
</style>
</head>
<body>
  <main class="canvas">
    <section class="window-graphic" aria-label="Brightmoor Security Solutions rear window graphic">
      <svg class="window-graphic__shape" viewBox="0 0 1231 433" preserveAspectRatio="none" aria-hidden="true">
        <path d="M318,0 L915,0 C1080,12 1162,150 1178,433 L53,433 C69,150 151,12 318,0 Z" fill="var(--white)"/>
        <path d="M260,25 C160,72 92,200 70,433 L94,433 C112,212 172,84 260,25 Z" fill="var(--slate)"/>
        <path d="M971,25 C1071,72 1139,200 1161,433 L1137,433 C1119,212 1059,84 971,25 Z" fill="var(--slate)"/>
      </svg>

      <div class="brand">
        <span class="brand__mark" aria-hidden="true"></span>
        <p class="brand__name">
          <span class="brand__name-main">BRIGHTMOOR</span>
          <span class="brand__name-sub">SECURITY SOLUTIONS</span>
        </p>
      </div>

      <p class="tagline">PROTECTION YOU<br>- CAN COUNT ON -</p>

      <div class="cta">
        <span class="cta__badge"><span class="cta__badge-text">CALL NOW</span></span>
        <p class="cta__service">FOR SERVICE</p>
        <p class="cta__phone">(206) 555-0147</p>
        <p class="cta__web">BRIGHTMOORSECURITYWA.EXAMPLE</p>
      </div>
    </section>
  </main>
</body>
</html>
```